'Brantley Electrical' web design

I need a web design for an electrical/electrician company based in sydney called brantley electrical. The logo design and business card design have been uploaded to be used on the web design. I want the design to be very modern and clean. I want the sector designs on the business card, i.e "residential", "commercial" etc, to be fleshed out on the front page. Base those sector designs off the business card but try to make them more minimal and modern to suit the website. Contact details are also on the business card. Try to suit the colour scheme of the logo. The sector designs should be up the top and linked so when clicked it will scroll down the website to brief descriptions of the work the company does in those sectors. I want the website to mainly attract builders, insurance companies and the commercial sector. I want the website to look unique. Custom graphics would be nice to make the website standout. I don't want the website to look like generic.

Target Market(s)

Builders, commercial sector, home owners

Industry/Entity Type

Electrical/Construction

Coding

Coded - Design and coding required

Number of Pages Required

3 page

Requirements
Must have
• Modern design
Nice to have
• Custom graphics that make the website unique

```html
<!DOCTYPE html>
<html lang="en">
<head>
<meta charset="utf-8">
<title>Brantley Electrical</title>
<link rel="stylesheet" href="https://fonts.googleapis.com/css2?family=Poppins:wght@600;700;800&family=Inter:wght@400;500;600;700&display=swap">
<style>
:root{
  --blue:#0d4fa0;
  --blue-dark:#0a3f86;
  --yellow:#fcc30b;
  --orange:#ee8252;
  --text:#555b66;
  --ink:#1d2230;
  --line:#e4e6ea;
  --white:#ffffff;
}
*{margin:0;padding:0;box-sizing:border-box}
html,body{width:1200px;height:5043px;overflow:hidden}
body{position:relative;background:var(--white);font-family:"Inter",sans-serif;color:var(--text)}
.abs{position:absolute}
.btn{position:absolute;display:flex;align-items:center;justify-content:center;gap:6px;height:42px;background:linear-gradient(90deg,var(--yellow),var(--orange));color:var(--white);font:700 13px "Inter",sans-serif;letter-spacing:.3px}
.btn .arr{width:13px;height:13px;border-radius:50%;background:var(--white);display:inline-flex;align-items:center;justify-content:center}
.btn .arr::after{content:"";border-left:5px solid var(--orange);border-top:3.5px solid transparent;border-bottom:3.5px solid transparent;margin-left:1px}
.para{font-size:13.5px;line-height:25.5px}
.h2{font:800 42px "Poppins",sans-serif;color:var(--blue);letter-spacing:.3px;line-height:1}

/* top bar */
.topbar{top:0;left:0;width:1200px;height:43px;background:var(--blue)}
.topbar .soc{top:12px;width:19px;height:19px;border-radius:50%;background:rgba(255,255,255,.9)}
.callbar{top:0;left:838px;width:274px;height:43px;background:var(--yellow);color:var(--ink);font-size:13px;display:flex;align-items:center;justify-content:center;gap:8px}
/* nav */
.nav{top:43px;left:0;width:1200px;height:65px;background:var(--white)}
.brand{top:58px;left:112px;display:flex;align-items:center;gap:10px;font:700 19px "Poppins",sans-serif;color:var(--blue)}
.brand i{width:30px;height:30px;background:var(--orange);display:block}
.menu{top:43px;left:462px;display:flex;height:65px;align-items:center}
.menu a{font-size:13px;color:var(--ink);text-decoration:none;margin-right:31px;text-transform:uppercase}
.menu a.on{color:var(--orange);position:relative}
.menu a.on::before{content:"";position:absolute;left:0;right:0;top:-22px;height:3px;background:var(--orange)}
/* hero */
.hero{top:108px;left:0;width:1200px;height:642px;overflow:hidden}
.hero-title{top:180px;left:110px;font:800 56px/1.05 "Poppins",sans-serif;color:var(--white)}
.hero-title span{color:var(--yellow);display:block}
.hero-text{top:316px;left:111px;width:300px;color:var(--white);font-size:14px;line-height:25px}
.hero-btn{top:410px;left:115px;width:180px;height:42px;clip-path:polygon(8% 0,92% 0,100% 50%,92% 100%,8% 100%,0 50%)}
/* about */
.about-img{top:869px;left:112px;width:426px;height:437px;background:radial-gradient(circle at 60% 25%,#e9eaea 0 8%,transparent 22%),radial-gradient(circle at 30% 70%,#6d7a8c,transparent 45%),linear-gradient(135deg,#a6abb1,#4a4f58 55%,#23262c)}
.about-bar{top:973px;left:538px;width:28px;height:216px;background:var(--orange)}
.callbox{top:1230px;left:84px;width:292px;height:107px;background:var(--yellow);display:flex;align-items:center;gap:18px;padding-left:28px}
.callbox small{display:block;font:600 13px "Inter",sans-serif;color:var(--ink)}
.callbox b{font:600 27px "Inter",sans-serif;color:var(--ink)}
/* sectors */
.photo{position:absolute}
.right-al{text-align:right}
/* testimonials */
.testi{top:3527px;left:0;width:1200px;height:556px;background:linear-gradient(90deg,var(--yellow),var(--orange))}
.testi h2{position:absolute;top:118px;width:1200px;text-align:center;font:800 42px "Poppins",sans-serif;color:var(--white)}
.card{position:absolute;top:197px;width:313px;height:212px;background:var(--white);padding:30px 26px}
.card .q{position:absolute;top:-26px;left:22px;font:800 72px/1 "Poppins",sans-serif;color:var(--orange)}
.card p{font-size:13.5px;line-height:25.5px;text-align:justify}
.card .who{margin-top:16px;font:700 17px "Inter",sans-serif;color:var(--ink)}
.card .who span{font:400 13px "Inter",sans-serif;color:var(--text);margin-left:8px}
.dots{position:absolute;top:441px;left:572px;display:flex;gap:6px}
.dots i{width:12px;height:12px;border-radius:50%;border:2px solid var(--white);display:block}
.dots i.on{background:var(--white);box-shadow:inset 0 0 0 2px var(--orange)}
/* contact */
.contact h2{position:absolute;top:4186px;width:1200px;text-align:center}
.info{position:absolute;top:4265px;width:260px;text-align:center}
.info .ic{width:44px;height:44px;border-radius:50%;background:linear-gradient(135deg,var(--yellow),var(--orange));margin:0 auto 8px;display:flex;align-items:center;justify-content:center}
.info small{display:block;font:600 13px "Inter",sans-serif;color:var(--blue)}
.info b{display:block;margin-top:6px;font:500 16px "Inter",sans-serif;color:var(--ink)}
.field{position:absolute;border:1px solid var(--line);font-size:11px;color:#666;padding:14px 20px}
/* footer */
.footer{top:4709px;left:0;width:1200px;height:334px;background:var(--blue)}
.f-brand{position:absolute;top:90px;width:1200px;display:flex;justify-content:center;align-items:center;gap:10px;font:700 22px "Poppins",sans-serif;color:var(--white)}
.f-brand i{width:34px;height:34px;background:var(--white);display:block}
.f-links{position:absolute;top:158px;width:1200px;text-align:center;font-size:13.5px;color:var(--white)}
.f-links span{margin:0 12px}
.f-soc{position:absolute;top:208px;left:527px;display:flex;gap:22px}
.f-soc i{width:22px;height:22px;border-radius:50%;background:var(--white);display:block}
.copy{position:absolute;top:268px;width:1200px;text-align:center;font-size:13.5px;color:var(--white)}
</style>
</head>
<body>

<header>
  <div class="abs topbar">
    <i class="abs soc" style="left:114px"></i>
    <i class="abs soc" style="left:145px"></i>
    <i class="abs soc" style="left:176px"></i>
    <i class="abs soc" style="left:207px"></i>
  </div>
  <div class="abs callbar">
    <svg width="13" height="13" viewBox="0 0 24 24"><path fill="#1d2230" d="M6.6 10.8a15 15 0 0 0 6.6 6.6l2.2-2.2c.3-.3.7-.4 1-.2 1.1.4 2.3.6 3.6.6.6 0 1 .4 1 1V20c0 .6-.4 1-1 1A17 17 0 0 1 3 4c0-.6.4-1 1-1h3.5c.6 0 1 .4 1 1 0 1.3.2 2.5.6 3.6.1.3 0 .7-.2 1z"/></svg>
    CALL US TODAY : +0412 555 019
  </div>
  <div class="abs nav"></div>
  <div class="abs brand"><i></i>BRANTLEY ELECTRICAL</div>
  <nav class="abs menu">
    <a class="on">Home</a><a>About us</a><a>Commercial</a><a>Contruction</a><a>Industrial</a><a>Residential</a>
  </nav>
</header>

<section class="abs hero">
  <svg width="1200" height="642" viewBox="0 0 1200 642" role="img" aria-label="Photo: electrician in hard hat working on wiring beside a blue-toned dining room interior">
    <defs>
      <linearGradient id="roomTone" x1="0" y1="0" x2="1" y2="1"><stop offset="0" stop-color="#2c5490"/><stop offset=".55" stop-color="#1a3a72"/><stop offset="1" stop-color="#0d2147"/></linearGradient>
      <radialGradient id="roomGlow" cx=".35" cy=".2" r=".5"><stop offset="0" stop-color="#6b8cc4" stop-opacity=".55"/><stop offset="1" stop-color="#6b8cc4" stop-opacity="0"/></radialGradient>
      <linearGradient id="workTone" x1="0" y1="0" x2="1" y2="1"><stop offset="0" stop-color="#b9573a"/><stop offset=".5" stop-color="#e7946a"/><stop offset="1" stop-color="#9b4a2a"/></linearGradient>
      <radialGradient id="workGlow" cx=".75" cy=".35" r=".45"><stop offset="0" stop-color="#f6c08e" stop-opacity=".7"/><stop offset="1" stop-color="#f6c08e" stop-opacity="0"/></radialGradient>
    </defs>
    <rect width="1200" height="642" fill="url(#roomTone)"/>
    <rect width="1200" height="642" fill="url(#roomGlow)"/>
    <polygon points="760,0 1200,0 1200,642 440,642" fill="url(#workTone)"/>
    <polygon points="760,0 1200,0 1200,642 440,642" fill="url(#workGlow)"/>
  </svg>
</section>
<h1 class="abs hero-title">BRANTLEY<span>ELECTRICAL</span></h1>
<p class="abs hero-text">Lorem ipsum dolor sit amet, consectetur adipiscing elit, seddo eius mod tempor ut labore et dolore magna aliqua.</p>
<a class="btn hero-btn">GET STARTED <span class="arr"></span></a>

<section class="about">
  <div class="abs about-bar"></div>
  <div class="abs about-img" role="img" aria-label="Photo: electrician in white hard hat and safety glasses working on a switchboard"></div>
  <div class="abs callbox">
    <svg width="38" height="38" viewBox="0 0 24 24"><path fill="none" stroke="#1d2230" stroke-width="1.8" d="M6.6 10.8a15 15 0 0 0 6.6 6.6l2.2-2.2c.3-.3.7-.4 1-.2 1.1.4 2.3.6 3.6.6.6 0 1 .4 1 1V20c0 .6-.4 1-1 1A17 17 0 0 1 3 4c0-.6.4-1 1-1h3.5c.6 0 1 .4 1 1 0 1.3.2 2.5.6 3.6.1.3 0 .7-.2 1z"/></svg>
    <div><small>CALL US :</small><b>+0412 555 019</b></div>
  </div>
  <h2 class="abs h2" style="top:866px;left:599px">BRANTLEY ELECTRICAL</h2>
  <p class="abs para" style="top:928px;left:599px;width:480px;text-align:justify">Lorem ipsum dolor sit amet, consectetur adipiscing elit, sed do eiusm od tempor incididunt ut labore et dolore magna aliqua. Ut enim ad mi nim veniam, quis nostrud exercitation ullamco laboris nisi ut aliquip ex ea commodo consequat. Duis aute irure dolor in reprehenderit in volu ptate velit esse cillum dolore eu fugiat nulla pariatur. Excepteur sint occaecat cupidatat non proident, sunt in culpa qui officia deserunt mollit anim id est laborum.</p>
  <p class="abs para" style="top:1133px;left:599px;width:480px;text-align:justify">Lorem ipsum dolor sit amet, consectetur adipiscing elit, sed do eiusmod tempor incididunt ut labore et dolore magna aliqua. Ut enim ad minim veniam, quis nostrud exercitation ullamco laboris nisi ut aliquip ex ea commodo consequat.</p>
  <a class="btn" style="top:1261px;left:599px;width:186px">LEARN MORE <span class="arr"></span></a>
</section>

<section class="sector">
  <div class="photo" style="top:1439px;left:603px;width:597px;height:521px;background:radial-gradient(ellipse at 70% 45%,#f4c98c 0,rgba(244,201,140,0) 35%),linear-gradient(180deg,#6f7788 0%,#c99a78 40%,#e0a66c 52%,#44608e 62%,#2d4670 100%);clip-path:polygon(17% 0,100% 0,100% 100%,0 100%)" role="img" aria-label="Photo: worker in hi-vis vest walking on a metal roof at sunset"></div>
  <h2 class="abs h2" style="top:1518px;left:114px">COMMERCIAL</h2>
  <p class="abs para" style="top:1580px;left:114px;width:478px;text-align:justify">Lorem ipsum dolor sit amet, consectetur adipiscing elit, sed do eiusm od tempor incididunt ut labore et dolore magna aliqua. Ut enim ad mi nim veniam, quis nostrud exercitation ullamco laboris nisi ut aliquip ex ea commodo consequat. Duis aute irure dolor in reprehenderit in volu ptate velit esse cillum dolore eu fugiat nulla pariatur. Excepteur sint occaecat cupidatat non proident, sunt in culpa qui officia deserunt mollit anim id est laborum. Lorem ipsum dolor sit amet, consectetur adipiscing elit, sed do eiusmod tempor incididunt ut labore et dolore magna aliqua. Ut enim ad minim veniam</p>
  <a class="btn" style="top:1836px;left:114px;width:184px">LEARN MORE <span class="arr"></span></a>
</section>

<section class="sector">
  <div class="photo" style="top:1960px;left:0;width:597px;height:523px;background:radial-gradient(circle at 62% 18%,#e0703c 0,rgba(224,112,60,0) 18%),radial-gradient(ellipse at 20% 30%,#c9d6e2,rgba(201,214,226,0) 40%),linear-gradient(135deg,#8aa2bb,#3a5a86 50%,#1f2d40);clip-path:polygon(0 0,100% 0,83% 100%,0 100%)" role="img" aria-label="Photo: worker in orange hard hat reading plans beside machinery"></div>
  <h2 class="abs h2 right-al" style="top:2039px;left:607px;width:480px">CONTRUCTION</h2>
  <p class="abs para right-al" style="top:2101px;left:607px;width:480px;text-align-last:right;text-align:justify">Lorem ipsum dolor sit amet, consectetur adipiscing elit, sed do eiusm od tempor incididunt ut labore et dolore magna aliqua. Ut enim ad mi nim veniam, quis nostrud exercitation ullamco laboris nisi ut aliquip ex ea commodo consequat. Duis aute irure dolor in reprehenderit in volu ptate velit esse cillum dolore eu fugiat nulla pariatur. Excepteur sint occaecat cupidatat non proident, sunt in culpa qui officia deserunt mollit anim id est laborum. Lorem ipsum dolor sit amet, consectetur adipiscing elit, sed do eiusmod tempor incididunt ut labore et dolore magna aliqua. Ut enim ad minim veniam</p>
  <a class="btn" style="top:2357px;left:901px;width:186px">LEARN MORE <span class="arr"></span></a>
</section>

<section class="sector">
  <div class="photo" style="top:2483px;left:603px;width:597px;height:523px;background:radial-gradient(circle at 55% 25%,#f2b833 0,rgba(242,184,51,0) 20%),radial-gradient(ellipse at 60% 65%,#dbe04a,rgba(219,224,74,0) 40%),linear-gradient(150deg,#9ba1a8,#7f8791 45%,#4f5763);clip-path:polygon(17% 0,100% 0,100% 100%,0 100%)" role="img" aria-label="Photo: two workers in hard hats and hi-vis vests reviewing plans in a warehouse"></div>
  <h2 class="abs h2" style="top:2563px;left:114px">INDUSTRIAL</h2>
  <p class="abs para" style="top:2625px;left:114px;width:478px;text-align:justify">Lorem ipsum dolor sit amet, consectetur adipiscing elit, sed do eiusm od tempor incididunt ut labore et dolore magna aliqua. Ut enim ad mi nim veniam, quis nostrud exercitation ullamco laboris nisi ut aliquip ex ea commodo consequat. Duis aute irure dolor in reprehenderit in volu ptate velit esse cillum dolore eu fugiat nulla pariatur. Excepteur sint occaecat cupidatat non proident, sunt in culpa qui officia deserunt mollit anim id est laborum. Lorem ipsum dolor sit amet, consectetur adipiscing elit, sed do eiusmod tempor incididunt ut labore et dolore magna aliqua. Ut enim ad minim veniam</p>
  <a class="btn" style="top:2881px;left:114px;width:184px">LEARN MORE <span class="arr"></span></a>
</section>

<section class="sector">
  <div class="photo" style="top:3006px;left:0;width:597px;height:521px;background:radial-gradient(ellipse at 40% 70%,#2f4a78 0,rgba(47,74,120,0) 22%),radial-gradient(ellipse at 45% 50%,#d9a441 0,rgba(217,164,65,0) 14%),linear-gradient(135deg,#f6f6f6,#dcdde0 55%,#b5b9c0);clip-path:polygon(0 0,100% 0,83% 100%,0 100%)" role="img" aria-label="Photo: electrician on a ladder installing a ceiling light in a white kitchen"></div>
  <h2 class="abs h2 right-al" style="top:3084px;left:607px;width:480px">RESIDENTIAL</h2>
  <p class="abs para right-al" style="top:3146px;left:607px;width:480px;text-align-last:right;text-align:justify">Lorem ipsum dolor sit amet, consectetur adipiscing elit, sed do eiusm od tempor incididunt ut labore et dolore magna aliqua. Ut enim ad mi nim veniam, quis nostrud exercitation ullamco laboris nisi ut aliquip ex ea commodo consequat. Duis aute irure dolor in reprehenderit in volu ptate velit esse cillum dolore eu fugiat nulla pariatur. Excepteur sint occaecat cupidatat non proident, sunt in culpa qui officia deserunt mollit anim id est laborum. Lorem ipsum dolor sit amet, consectetur adipiscing elit, sed do eiusmod tempor incididunt ut labore et dolore magna aliqua. Ut enim ad minim veniam</p>
  <a class="btn" style="top:3402px;left:901px;width:186px">LEARN MORE <span class="arr"></span></a>
</section>

<section class="abs testi">
  <h2>TESTIMONIALS</h2>
  <div class="card" style="left:112px"><span class="q">&ldquo;</span><p>Lorem ipsum dolor sit amet, conse ctet uradipiscing elit, sed do eiusm od tempor incididunt ut labore et dolore magna aliqua. Ut enim ad mi nim veniam, quis nostrud</p><div class="who">John doe<span>Company name</span></div></div>
  <div class="card" style="left:444px"><span class="q">&ldquo;</span><p>Lorem ipsum dolor sit amet, conse ctet uradipiscing elit, sed do eiusm od tempor incididunt ut labore et dolore magna aliqua. Ut enim ad mi nim veniam, quis nostrud</p><div class="who">John doe<span>Company name</span></div></div>
  <div class="card" style="left:775px"><span class="q">&ldquo;</span><p>Lorem ipsum dolor sit amet, conse ctet uradipiscing elit, sed do eiusm od tempor incididunt ut labore et dolore magna aliqua. Ut enim ad mi nim veniam, quis nostrud</p><div class="who">John doe<span>Company name</span></div></div>
  <div class="dots"><i></i><i class="on"></i><i></i></div>
</section>

<section class="contact">
  <h2 class="h2">CONTACT US</h2>
  <div class="info" style="left:183px">
    <div class="ic"><svg width="16" height="16" viewBox="0 0 24 24"><path fill="#fff" d="M12 2a7 7 0 0 0-7 7c0 5 7 13 7 13s7-8 7-13a7 7 0 0 0-7-7zm0 9.5A2.5 2.5 0 1 1 12 6.5a2.5 2.5 0 0 1 0 5z"/></svg></div>
    <small>Address :</small><b>123,Lorem ipsum dolor sit</b>
  </div>
  <div class="info" style="left:461px">
    <div class="ic"><svg width="16" height="16" viewBox="0 0 24 24"><path fill="#fff" d="M6.6 10.8a15 15 0 0 0 6.6 6.6l2.2-2.2c.3-.3.7-.4 1-.2 1.1.4 2.3.6 3.6.6.6 0 1 .4 1 1V20c0 .6-.4 1-1 1A17 17 0 0 1 3 4c0-.6.4-1 1-1h3.5c.6 0 1 .4 1 1 0 1.3.2 2.5.6 3.6.1.3 0 .7-.2 1z"/></svg></div>
    <small>Phone :</small><b>+0412 555 019</b>
  </div>
  <div class="info" style="left:739px">
    <div class="ic"><svg width="16" height="16" viewBox="0 0 24 24"><path fill="#fff" d="M3 5h18v14H3zm2 2v.5l7 5 7-5V7l-7 5z"/></svg></div>
    <small>Email :</small><b>hello@brantleymail.com</b>
  </div>
  <div class="field" style="top:4390px;left:206px;width:246px;height:45px">Name</div>
  <div class="field" style="top:4390px;left:466px;width:249px;height:45px">Email address</div>
  <div class="field" style="top:4390px;left:728px;width:247px;height:45px">Phone</div>
  <div class="field" style="top:4449px;left:206px;width:769px;height:101px">Message</div>
  <a class="btn" style="top:4566px;left:529px;width:143px;font-size:10px">SUBMIT NOW</a>
</section>

<footer class="abs footer">
  <div class="f-brand"><i></i>BRANTLEY ELECTRICAL</div>
  <div class="f-links">HOME<span>/</span>ABOUT US<span>/</span>COMMERCIAL<span>/</span>CONTRUCTION<span>/</span>INDUSTRIAL<span>/</span>RESIDENTIAL</div>
  <div class="f-soc"><i></i><i></i><i></i><i></i></div>
  <div class="copy">&copy; Copyrights 2023 Brantley Electrical | All Rights Reserved</div>
</footer>

</body>
</html>
```